VorBlend Advantages & Features Advertising

We are VorBlend, a manufacturer offering complete mixing solutions for all industries since 1954. Our engineering & innovation, combined with our performance & quality, value & pricing, backed with the best warranty in the industry has made us the most disruptive brand in the industry.

We need to create an add that promotes our diversity across the Pharmaceutical & Nutraceutical, Food & Beverage, Bakery & Confectionary, Chemical, and Cosmetic / Health & Beauty industries

We need a professional, energetic, and captivating ad the captures the attention of the customer while branding our product.

I have included our logo, along with some png pictures for use.

Our website is www.vorblendco.example and our YouTube channel is you want to find out more about us is https://www.video.example/channel/UCqzTowkL4DMAsYxhaRPiOkb

I have also included our Answers Led Booklet

Please feel free to write if you have any questions

Our engineering & innovation allow us to remain leaders in the industry with our products. Our Merit Built Design allow us to capture the heart of our customers as we include features that allow us to meet the demands of today, while keeping in mind the needs of tomorrow.

Our performance & quality allow us to go head to head with our competition and win while allowing a quick ROI for our customers on their investment

Our value and pricing allow us to meet or exceed our competitors performance & specifications while beating them in price, warranty, and customer service. Exceeding the expectations of customers globally

Target Market(s)

Pharmaceutical & Nutraceutical manufacturers, Food & Beverage manufacturers, Cosmetic & Health/Beauty manufacturers, & Chemical manufacturers

Industry/Entity Type

Manufacturer

Requirements
Must have
• Energy & capture the attention of customer with a focus on branding
Nice to have
• www.vorblendco.example website

```html
<!DOCTYPE html>
<html lang="en">
<head>
<meta charset="utf-8">
<title>VorBlend – Industrial Mixers</title>
<link href="https://fonts.googleapis.com/css2?family=Montserrat:wght@500;600;700;800&family=Open+Sans:wght@400;600&display=swap" rel="stylesheet">
<style>
:root{
  --red:#d9262e;
  --red-dark:#b51c23;
  --ink:#2b2f36;
  --muted:#6b7079;
  --blue:#1f8fd6;
  --teal:#27b3c8;
  --green:#3cc99a;
  --hero-bg:#eceef0;
  --white:#ffffff;
}
*{margin:0;padding:0;box-sizing:border-box}
html,body{width:747px;height:1200px;overflow:hidden;background:var(--white)}
body{position:relative;font-family:"Open Sans",Arial,sans-serif;color:var(--ink)}
.abs{position:absolute}
.head-font{font-family:"Montserrat",Arial,sans-serif}

/* header */
.site-header{top:0;left:0;width:747px;height:95px;background:var(--white)}
.brand{display:flex;align-items:center;gap:6px;font-family:"Montserrat",sans-serif;font-weight:800;font-size:21px;color:var(--red)}
.brand-dot{width:14px;height:14px;border-radius:50%;background:var(--red)}
.site-header .brand{position:absolute;left:38px;top:16px}
.contact{position:absolute;top:16px;display:flex;align-items:center;gap:6px}
.contact-icon{width:20px;height:20px;border-radius:4px;background:var(--blue);display:flex;align-items:center;justify-content:center}
.contact-text{font-size:6.5px;line-height:1.35;color:var(--muted)}
.contact-text b{display:block;color:var(--ink);font-weight:600}
.main-nav{position:absolute;top:66px;left:190px;font-family:"Montserrat",sans-serif;font-weight:700;font-size:8.5px;color:var(--ink);letter-spacing:.2px;word-spacing:2px}
.social{position:absolute;top:64px;left:585px;display:flex;gap:8px}
.social span{width:11px;height:11px;border-radius:50%;background:#5a5f68}
.header-rule{position:absolute;left:0;top:94px;width:747px;height:1px;background:#e3e5e8}

/* hero */
.hero{top:95px;left:0;width:747px;height:300px;background:linear-gradient(90deg,#f4f5f6 0%,var(--hero-bg) 55%,#e2e5e8 100%)}
.hero h1{position:absolute;left:40px;top:68px;width:330px;font-family:"Montserrat",sans-serif;font-weight:700;font-size:21px;line-height:1.3;color:var(--ink)}
.hero p{position:absolute;left:40px;top:140px;width:280px;font-size:7.5px;line-height:1.55;color:var(--muted)}
.photo{position:absolute;border-radius:2px}

/* industries band */
.industries{top:395px;left:0;width:747px;height:115px;display:flex;background:linear-gradient(90deg,var(--teal),var(--green))}
.industry{flex:1;display:flex;align-items:center;justify-content:center;gap:8px;padding:0 10px;color:var(--white)}
.industry:nth-child(1){background:rgba(0,70,110,.18)}
.industry:nth-child(3){background:rgba(255,255,255,.06)}
.industry h3{font-family:"Montserrat",sans-serif;font-weight:700;font-size:11px;line-height:1.25}

/* why */
.why-title{top:530px;left:0;width:747px;text-align:center;font-family:"Montserrat",sans-serif;font-weight:700;font-size:22px;color:var(--ink)}
.why-intro{top:568px;left:110px;width:527px;text-align:center;font-size:7px;line-height:1.6;color:var(--muted)}
.feature{position:absolute;width:205px}
.feature-head{display:flex;align-items:center;gap:7px;margin-bottom:6px}
.feature-icon{width:24px;height:24px;border-radius:50%;background:var(--red);display:flex;align-items:center;justify-content:center;flex:none}
.feature h4{font-family:"Montserrat",sans-serif;font-weight:700;font-size:12px;color:var(--ink)}
.feature p{font-size:7px;line-height:1.6;color:var(--muted);padding-left:31px}

/* stats */
.stats{top:880px;left:0;width:747px;height:320px;background:radial-gradient(ellipse at 80% 40%,#e5474d 0%,var(--red) 45%,var(--red-dark) 100%)}
.stat{position:absolute;top:78px;width:150px;text-align:center;color:var(--white)}
.stat svg{display:block;margin:0 auto 10px}
.stat strong{display:block;font-family:"Montserrat",sans-serif;font-weight:700;font-size:27px;line-height:1.1}
.stat span{display:block;font-family:"Montserrat",sans-serif;font-weight:500;font-size:10px;line-height:1.3;margin-top:3px}
.stats .brand{position:absolute;left:0;width:747px;justify-content:center;top:262px;color:var(--white)}
.stats .brand-dot{background:var(--white)}
</style>
</head>
<body>

<header class="abs site-header">
  <div class="brand"><span class="brand-dot"></span>VorBlend</div>

  <div class="contact" style="left:258px">
    <div class="contact-icon"><svg width="11" height="8" viewBox="0 0 11 8"><rect x=".5" y=".5" width="10" height="7" fill="none" stroke="#fff"/><path d="M.5 .5 5.5 4.5 10.5 .5" fill="none" stroke="#fff"/></svg></div>
    <div class="contact-text"><b>Email Us</b>info@vorblendco.example</div>
  </div>
  <div class="contact" style="left:372px">
    <div class="contact-icon"><svg width="9" height="11" viewBox="0 0 9 11"><rect x=".5" y=".5" width="8" height="10" rx="1.5" fill="none" stroke="#fff"/></svg></div>
    <div class="contact-text"><b>Phone</b>+1 555 010 2040</div>
  </div>
  <div class="contact" style="left:470px">
    <div class="contact-icon"><svg width="10" height="10" viewBox="0 0 10 10"><path d="M2 1 4 3 3 4.5Q4.5 6.5 5.5 7L7 6 9 8 7.5 9.5Q3 9 .5 2.5Z" fill="#fff"/></svg></div>
    <div class="contact-text"><b>Call Us</b>+1 555 010 2041</div>
  </div>

  <nav class="main-nav">Power Blenders &amp; Dryers · Paste Kneaders &amp; Mixers · Liquid Dispersers &amp; Mixers</nav>
  <div class="social"><span></span><span></span><span></span><span></span><span></span></div>
  <div class="header-rule"></div>
</header>

<section class="abs hero">
  <h1>Industrial Mixer, Mixing Equipment &amp; Powder Mixers</h1>
  <p>We are VorBlend, a manufacturer offering complete mixing solutions for all industries since 1954. Our engineering &amp; innovation, combined with our performance &amp; quality, value &amp; pricing, backed with the best warranty in the industry has made us the most disruptive brand in the industry.</p>

  <div class="photo" role="img" aria-label="Laboratory and pharmaceutical tablets" style="left:440px;top:10px;width:90px;height:280px;background:linear-gradient(180deg,#c9d3dc,#8aa0b3 45%,#dfe4ea)"></div>
  <div class="photo" role="img" aria-label="Stainless steel powder mixer" style="left:536px;top:10px;width:90px;height:280px;background:linear-gradient(180deg,#dfe3e7,#a7b1ba 50%,#e8ebee)"></div>
  <div class="photo" role="img" aria-label="Cosmetic cream products" style="left:632px;top:10px;width:84px;height:137px;background:linear-gradient(180deg,#f1e4e6,#d9bcc3)"></div>
  <div class="photo" role="img" aria-label="Industrial mixing vessel" style="left:632px;top:153px;width:84px;height:137px;background:linear-gradient(180deg,#c6ced6,#7f8c99)"></div>
</section>

<section class="abs industries">
  <div class="industry">
    <svg width="28" height="28" viewBox="0 0 28 28" fill="none" stroke="#fff" stroke-width="1.6"><path d="M10 3h8M11 3v8L5 23q-1 3 2 3h14q3 0 2-3l-6-12V3"/><path d="M8 18h12"/></svg>
    <h3>Pharmaceutical &amp; Nutraceutical manufacturers</h3>
  </div>
  <div class="industry">
    <svg width="28" height="28" viewBox="0 0 28 28" fill="none" stroke="#fff" stroke-width="1.6"><path d="M4 12h20l-2 12H6Z"/><path d="M9 12V7M14 12V4M19 12V7"/></svg>
    <h3>Food &amp; Beverage manufacturers</h3>
  </div>
  <div class="industry">
    <svg width="28" height="28" viewBox="0 0 28 28" fill="none" stroke="#fff" stroke-width="1.6"><rect x="9" y="10" width="10" height="15" rx="2"/><rect x="11" y="4" width="6" height="6"/></svg>
    <h3>Cosmetic &amp; Health Beauty manufacturers</h3>
  </div>
  <div class="industry">
    <svg width="28" height="28" viewBox="0 0 28 28" fill="none" stroke="#fff" stroke-width="1.6"><circle cx="14" cy="18" r="7"/><path d="M12 11V4h4v7"/></svg>
    <h3>Chemical manufacturers</h3>
  </div>
</section>

<h2 class="abs why-title">Why Choose Us ?</h2>
<p class="abs why-intro">VorBlend Co. has been a dependable maker of mixing and processing equipment for decades. We supply powder blenders, paste kneaders and liquid dispersers built for every industry, engineered to last and priced to give real value to every customer worldwide.</p>

<div class="feature" style="left:52px;top:625px">
  <div class="feature-head"><span class="feature-icon"><svg width="12" height="12" viewBox="0 0 12 12"><circle cx="6" cy="5" r="3.5" fill="none" stroke="#fff" stroke-width="1.3"/><path d="M4.5 10h3" stroke="#fff" stroke-width="1.3"/></svg></span><h4>Clever Innovations</h4></div>
  <p>Our engineering &amp; innovation allow us to remain leaders in the industry with our products.</p>
</div>
<div class="feature" style="left:495px;top:625px">
  <div class="feature-head"><span class="feature-icon"><svg width="12" height="12" viewBox="0 0 12 12"><circle cx="6" cy="4" r="2.5" fill="#fff"/><path d="M1.5 11q4.5-6 9 0" fill="#fff"/></svg></span><h4>Best Engineers</h4></div>
  <p>Our Merit Built Design allow us to capture the heart of our customers as we include features that meet the demands of today, while keeping in mind the needs of tomorrow.</p>
</div>
<div class="feature" style="left:52px;top:745px">
  <div class="feature-head"><span class="feature-icon"><svg width="12" height="12" viewBox="0 0 12 12"><path d="M2 6.5 5 9.5 10 3" fill="none" stroke="#fff" stroke-width="1.6"/></svg></span><h4>Performance &amp; Quality</h4></div>
  <p>Our performance &amp; quality allow us to go head to head with our competition and win while allowing a quick ROI for our customers on their investment.</p>
</div>
<div class="feature" style="left:495px;top:745px">
  <div class="feature-head"><span class="feature-icon"><svg width="12" height="12" viewBox="0 0 12 12"><path d="M6 1v10M8.5 3.5Q6 2 4 3.5T6 6t2 2.5T3.5 8.5" fill="none" stroke="#fff" stroke-width="1.3"/></svg></span><h4>"Made-in-China" prices</h4></div>
  <p>Our value and pricing allow us to meet or exceed our competitors performance &amp; specifications while beating them in price, warranty, and customer service.</p>
</div>

<div class="photo" role="img" aria-label="Stainless steel industrial mixer machine" style="left:275px;top:640px;width:200px;height:215px;background:radial-gradient(ellipse at 50% 50%,#d7dce1 0%,#a9b2bb 50%,rgba(255,255,255,0) 72%)"></div>

<section class="abs stats" role="img" aria-label="Red band over a photo of a worker in a factory">
  <div class="stat" style="left:55px">
    <svg width="32" height="32" viewBox="0 0 32 32" fill="none" stroke="#fff" stroke-width="1.6"><circle cx="16" cy="11" r="5"/><path d="M6 28q10-16 20 0"/></svg>
    <strong>1000+</strong><span>Happy<br>Customers</span>
  </div>
  <div class="stat" style="left:215px">
    <svg width="32" height="32" viewBox="0 0 32 32" fill="none" stroke="#fff" stroke-width="1.6"><circle cx="16" cy="16" r="5"/><path d="M16 3v5M16 24v5M3 16h5M24 16h5M7 7l3.5 3.5M21.5 21.5 25 25M7 25l3.5-3.5M21.5 10.5 25 7"/></svg>
    <strong>50+</strong><span>Individual<br>Machineries</span>
  </div>
  <div class="stat" style="left:375px">
    <svg width="32" height="32" viewBox="0 0 32 32" fill="none" stroke="#fff" stroke-width="1.6"><path d="M6 18v-3a10 10 0 0 1 20 0v3"/><rect x="4" y="18" width="5" height="8" rx="1"/><rect x="23" y="18" width="5" height="8" rx="1"/></svg>
    <strong>24 / 7</strong><span>Customer<br>Support</span>
  </div>
  <div class="stat" style="left:540px">
    <svg width="32" height="32" viewBox="0 0 32 32" fill="none" stroke="#fff" stroke-width="1.6"><path d="M11 28h10M12 24h8M12 24q0-4-3-7a8 8 0 1 1 14 0q-3 3-3 7"/></svg>
    <strong>10+</strong><span>New<br>Innovations</span>
  </div>
  <div class="brand"><span class="brand-dot"></span>VorBlend</div>
</section>

</body>
</html>
```